Business Consulting Company requires a website design (PSD+HTML+CSS required)

Marlowe Advisory is a Business Consulting Company that provides Analysis, Business Coaching and Systems and Document Design for clients.

We would like a simplistic yet professional looking website design that uses high quality imagery to project a professional persona across our entire site.

The completed project will need to include PSD files (for editing in Photoshop) and will need to also include HTML+CSS coded files that can be edited in Adobe Dreamweaver CS5.5.

Marlowe Advisory currently has a functioning website (located at www.marloweadvisory-example.com.au) but would like to replace its current site with something more professional, user friendly and content simplistic, with the overall design of this project being clean and very easy to navigate whilst remaining professionally focused.

A brief has been attached to this project to provide the key details but please feel free to contact me if you require any clarification or have any questions regarding the project.

Target Market(s)

The target audience for this website will be small to medium sized businesses (of all descriptions).

Industry/Entity Type

Business

Coding

Coded - Design and coding required

Number of Pages Required

5+ page

Requirements
Must have
• Simplistic design structure
• Professional images
• Easy to navigate
• Must be uploaded in PSD format
• Must be coded (HTML+CSS) and compatible with Adobe Dreamweaver CS5.5
Nice to have
• Use of the Company’s corporate colours throughout the site design
• Adding a Home page slider bar with images and short catchy messages (i.e. text based statements)
• Having a quick link box on each page that provides easy navigation throughout the site
• The use of different icons and images to depict our different services (i.e. a different icon and image for analysis service and coaching service etc.).
• All pages should follow a similar theme (universal approach to all pages)
Should not have
• When coding, images should not be used in place of text (all text must be editable)

```html
<!DOCTYPE html>
<html lang="en">
<head>
<meta charset="utf-8">
<title>Marlowe Advisory</title>
<link href="https://fonts.googleapis.com/css2?family=Open+Sans:wght@400;600;700;800&family=Oswald:wght@400&display=swap" rel="stylesheet">
<style>
:root{
  --blue:#1b9ad8;
  --blue-dark:#1584bb;
  --ink:#333;
  --muted:#666;
  --grey-band:#e1e1e1;
  --charcoal:#555758;
  --dark:#1b1d20;
  --white:#fff;
}
*{box-sizing:border-box;margin:0;padding:0}
html,body{width:1200px;height:4698px;overflow:hidden}
body{font-family:"Open Sans",Arial,sans-serif;color:var(--ink);background:var(--white);font-size:15px;line-height:1.5}
.wrap{width:960px;margin:0 auto;position:relative}
.section-title{font-size:44px;font-weight:700;color:var(--blue);letter-spacing:.5px;line-height:1.1}
.section-title::after{content:"";display:block;width:150px;height:3px;background:var(--blue);margin-top:10px}

/* header */
.site-header{height:155px;display:flex;align-items:center}
.site-header .wrap{display:flex;justify-content:space-between;align-items:center}
.brand{display:flex;align-items:center;gap:12px}
.brand-dot{width:34px;height:34px;border-radius:50%;background:#9aa0a6}
.brand-name{font-size:22px;font-weight:700;color:#6d7278;letter-spacing:1px}
.main-nav{display:flex;align-items:center;gap:26px;font-size:14px}
.main-nav a{color:#555;text-decoration:none}
.main-nav a.active{color:var(--blue);border-bottom:2px solid var(--blue);padding-bottom:3px}
.search-box{width:120px;height:22px;border:1px solid #ccc;background:#eee}

/* hero */
.hero{height:518px;position:relative;background:#0d0f13;overflow:hidden}
.hero-image{position:absolute;inset:0;background:radial-gradient(ellipse at 62% 70%,#a9c7e6 0%,#3f5f86 18%,#13161c 48%,#060709 100%)}
.hero-text{position:absolute;left:120px;top:50px;color:var(--white)}
.hero-text h1{font-size:42px;font-weight:600;letter-spacing:1px}
.hero-text p{font-size:14px;line-height:1.4;max-width:430px;margin-top:4px}
.hero-text a{display:inline-block;margin-top:30px;color:var(--blue);font-size:13px;font-weight:700;text-decoration:none}
.hero-strip{position:absolute;right:70px;top:0;width:52px;height:100%;background:linear-gradient(#d7e6f2,#7fa9cb)}

/* welcome */
.welcome{height:653px;background:var(--blue);color:var(--white);padding-top:50px}
.welcome h2{font-size:40px;font-weight:700}
.welcome .rule{height:1px;background:rgba(255,255,255,.6);margin:16px 0 26px}
.welcome p{font-size:15px;max-width:940px;margin-bottom:18px}
.features{display:flex;justify-content:space-between;margin-top:40px;padding:0 20px}
.feature{width:200px;text-align:center}
.feature-icon{width:104px;height:104px;border:3px solid var(--white);border-radius:50%;margin:0 auto 18px;display:flex;align-items:center;justify-content:center}
.feature h3{font-size:28px;font-weight:800;line-height:1}
.feature span{display:block;font-size:15px;font-weight:700;margin-top:4px}
.feature-go{width:20px;height:20px;border-radius:50%;background:var(--white);margin:22px auto 0;display:flex;align-items:center;justify-content:center}

/* services */
.services{height:502px;background:var(--grey-band);padding-top:44px}
.services-body{display:flex;justify-content:space-between;margin-top:28px}
.services-intro{width:410px;font-size:15px;color:#444}
.services-intro p{margin-bottom:18px}
.read-more{color:var(--blue);font-size:13px;font-weight:600;text-decoration:none;display:block;text-align:right;margin-top:8px}
.service-grid{width:500px;display:grid;grid-template-columns:1fr 1fr;gap:30px 30px}
.service{display:flex;gap:12px}
.service-icon{flex:none;width:54px;height:54px;border:2px solid var(--blue);border-radius:50%}
.service h4{font-size:11px;color:var(--blue);font-weight:700;text-transform:uppercase}
.service p{font-size:11px;color:#555;line-height:1.45}

/* about */
.about{height:734px;padding-top:34px}
.about-lead{font-size:15px;margin-top:24px;color:#444}
.team{display:flex;justify-content:space-between;margin-top:38px}
.member{width:290px}
.member-top{display:flex;align-items:center;gap:14px}
.member-photo{width:158px;height:158px;border-radius:50%;background:#c9c9c9}
.member-photo.first{background:linear-gradient(#8a8f95,#4b4f55)}
.socials{display:flex;gap:8px}
.soc{width:28px;height:28px;border-radius:50%;background:var(--blue)}
.member h5{font-size:11px;font-weight:700;margin-top:20px;text-transform:uppercase;color:#555}
.member .role{font-size:10px;color:#888}
.member p{font-size:11px;color:#555;margin-top:10px;line-height:1.5}

/* quick links */
.quick-links{height:253px;background:var(--charcoal);display:flex;align-items:center}
.quick-links .wrap{display:flex;justify-content:space-between;padding:0 10px}
.quick-link{width:200px;text-align:center;color:var(--white);font-size:18px;text-transform:uppercase}
.quick-link svg{display:block;margin:0 auto 10px}

/* products */
.products{height:829px;padding-top:54px}
.products-lead{font-size:15px;margin-top:26px;color:#444;max-width:930px}
.product-cols{display:flex;justify-content:space-between;margin-top:30px}
.product-col{width:440px}
.product{display:flex;gap:18px;margin-bottom:40px}
.product-icon{flex:none;width:48px;height:60px}
.product h4{font-size:18px;color:var(--blue);font-weight:600;text-transform:uppercase}
.product ul{list-style:none;font-size:14px;color:#444;line-height:1.55;margin-top:6px}
.products-next{width:26px;height:26px;border-radius:50%;background:var(--blue);position:absolute;right:0;top:620px}

/* clients */
.clients{height:273px;background:var(--charcoal);padding-top:14px}
.clients h2{font-family:"Oswald",sans-serif;color:var(--white);text-align:center;font-weight:400;font-size:30px}
.client-row{display:flex;gap:34px;margin:36px 0 0 40px}
.client{width:140px;height:96px;background:var(--blue);display:flex;align-items:center;justify-content:center;text-align:center;font-size:14px;font-weight:700;color:var(--blue-dark)}
.client.named{background:var(--white)}

/* contact */
.contact{height:522px;background:var(--grey-band);padding-top:44px}
.contact-body{display:flex;justify-content:space-between;margin-top:36px}
.contact-details{font-size:14px;color:#333;line-height:1.6}
.contact-details dt{font-weight:700;text-transform:uppercase}
.contact-details .row{display:flex;gap:20px}
.contact-form{width:322px;display:flex;flex-direction:column;gap:22px}
.field{background:var(--white);border:1px solid #aaa;height:38px;font-size:11px;color:#666;padding:10px 12px;text-transform:uppercase}
.field.message{height:90px}
.submit{align-self:flex-end;width:240px;height:40px;background:var(--white);border:1px solid #aaa;display:flex;align-items:center;justify-content:center;gap:8px;font-size:12px;color:#666}
.contact-social{display:flex;gap:12px;margin-top:-30px}
.contact-social span{width:20px;height:20px;border-radius:50%;background:var(--blue)}

/* footer */
.site-footer{height:259px;background:var(--dark);display:flex;flex-direction:column;align-items:center;justify-content:center;gap:14px;color:#aaa;font-size:12px}
.site-footer .brand-name{color:var(--white)}
.site-footer .brand-dot{background:var(--white)}
</style>
</head>
<body>

<header class="site-header">
  <div class="wrap">
    <div class="brand"><span class="brand-dot"></span><span class="brand-name">MARLOWE ADVISORY</span></div>
    <nav class="main-nav">
      <a class="active" href="#">Home</a><a href="#">About Us</a><a href="#">Services</a><a href="#">Testimonials</a><a href="#">Contact Us</a>
      <span class="search-box"></span>
    </nav>
  </div>
</header>

<section class="hero">
  <div class="hero-image" role="img" aria-label="Hands reaching toward a bright burst of light on a dark background"></div>
  <div class="hero-strip" role="img" aria-label="Slide preview thumbnail"></div>
  <div class="hero-text">
    <h1>EMPOWERMENT@WORK</h1>
    <p>Our leaders aren't following industry trends, they're setting them. Get access to Executive Insights, published articles and more.</p>
    <a href="#">VISIT OUR KNOWLEDGE CENTRE ›</a>
  </div>
</section>

<section class="welcome">
  <div class="wrap">
    <h2>Welcome to Marlowe Advisory!</h2>
    <div class="rule"></div>
    <p>Marlowe Advisory is a business analysis, coaching and business development provider who specialises in assisting businesses to achieve maximum efficiency, increased productivity and who can assist with improving a business's overall profitability.</p>
    <p>At Marlowe Advisory, we pride ourselves on our ability to form strong client relationships whilst delivering impressive results. For us, it's all about effective communication coupled with practical and measurable results!</p>
    <div class="features">
      <div class="feature">
        <div class="feature-icon"><svg width="54" height="54" viewBox="0 0 54 54" fill="none" stroke="#fff" stroke-width="3"><circle cx="27" cy="27" r="22"/><ellipse cx="27" cy="27" rx="10" ry="22"/><line x1="5" y1="27" x2="49" y2="27"/></svg></div>
        <h3>GLOBAL</h3><span>BUSINESS<br>GUIDE</span>
        <div class="feature-go"><svg width="8" height="8" viewBox="0 0 8 8"><path d="M2 1l4 3-4 3z" fill="#1b9ad8"/></svg></div>
      </div>
      <div class="feature">
        <div class="feature-icon"><svg width="54" height="54" viewBox="0 0 54 54" fill="none" stroke="#fff" stroke-width="3"><path d="M27 6a14 14 0 0 0-8 25v7h16v-7a14 14 0 0 0-8-25z"/><line x1="21" y1="44" x2="33" y2="44"/></svg></div>
        <h3>FRESH</h3><span>BUSINESS<br>IDEAS</span>
        <div class="feature-go"><svg width="8" height="8" viewBox="0 0 8 8"><path d="M2 1l4 3-4 3z" fill="#1b9ad8"/></svg></div>
      </div>
      <div class="feature">
        <div class="feature-icon"><svg width="54" height="54" viewBox="0 0 54 54" fill="none" stroke="#fff" stroke-width="3"><rect x="8" y="16" width="38" height="28" rx="3"/><path d="M20 16v-6h14v6"/></svg></div>
        <h3>PRO</h3><span>SERVICES &amp;<br>ADVICE</span>
        <div class="feature-go"><svg width="8" height="8" viewBox="0 0 8 8"><path d="M2 1l4 3-4 3z" fill="#1b9ad8"/></svg></div>
      </div>
      <div class="feature">
        <div class="feature-icon"><svg width="54" height="54" viewBox="0 0 54 54" fill="none" stroke="#fff" stroke-width="3"><circle cx="27" cy="27" r="21"/><path d="M27 14v13l9 6"/></svg></div>
        <h3>FAST</h3><span>ONLINE<br>SUPPORT</span>
        <div class="feature-go"><svg width="8" height="8" viewBox="0 0 8 8"><path d="M2 1l4 3-4 3z" fill="#1b9ad8"/></svg></div>
      </div>
    </div>
  </div>
</section>

<section class="services">
  <div class="wrap">
    <h2 class="section-title">OUR SERVICES</h2>
    <div class="services-body">
      <div class="services-intro">
        <p>Understanding that every one of our client's business needs are unique, Marlowe Advisory delivers four business services packages that can be specifically tailored to suit the individual needs of each of our customers.</p>
        <p>All our business services packages can be undertaken individually or can be combined to achieve maximum profitability and productivity gains for any business.</p>
        <a class="read-more" href="#">Read more »</a>
      </div>
      <div class="service-grid">
        <div class="service"><span class="service-icon"></span><div><h4>Business Analysis</h4><p>A clear review of your processes, finances and staffing to uncover the hidden costs slowing growth.</p></div></div>
        <div class="service"><span class="service-icon"></span><div><h4>Business Coaching</h4><p>Guided one-on-one sessions that build leadership skills, sharpen focus and keep goals firmly on track.</p></div></div>
        <div class="service"><span class="service-icon"></span><div><h4>Systems &amp; Document Design</h4><p>Practical templates, policies and procedures that bring order and consistency to daily operations.</p></div></div>
        <div class="service"><span class="service-icon"></span><div><h4>Business Development Planning</h4><p>Strategic plans that map out new markets, measurable targets and the steps needed to reach them.</p></div></div>
      </div>
    </div>
  </div>
</section>

<section class="about">
  <div class="wrap">
    <h2 class="section-title">ABOUT US</h2>
    <p class="about-lead">Marlowe Advisory is a business analysis, business coaching and business development specialist who provides uniquely tailored business solutions to large, medium and small businesses. Utilising our unique combination of enhanced communication techniques, detailed business analysis methods and years of personal experience allows us to achieve immediate maximum efficiency, productivity and profitability gains for our clients. So, if you believe that your business could benefit from a "smarter not harder" approach to its business operations, then Marlowe Advisory is the right choice!</p>
    <div class="team">
      <div class="member">
        <div class="member-top"><div class="member-photo first" role="img" aria-label="Portrait of the managing director"></div><div class="socials"><span class="soc"></span><span class="soc"></span><span class="soc"></span></div></div>
        <h5>Daniel Reyes</h5><div class="role">Managing Director &amp; Senior Consultant</div>
        <p>Daniel has years of experience in the fields of business coaching and management across many industries and leads every client project personally.</p>
        <a class="read-more" href="#">Read more »</a>
      </div>
      <div class="member">
        <div class="member-top"><div class="member-photo" role="img" aria-label="Team member photo placeholder"></div><div class="socials"><span class="soc"></span><span class="soc"></span><span class="soc"></span></div></div>
        <h5>Lorem Ipsum</h5><div class="role">Consultant</div>
        <p>Experienced business analyst who works closely with owners to review systems and map clear improvements for growth.</p>
      </div>
      <div class="member">
        <div class="member-top"><div class="member-photo" role="img" aria-label="Team member photo placeholder"></div><div class="socials"><span class="soc"></span><span class="soc"></span><span class="soc"></span></div></div>
        <h5>Lorem Ipsum</h5><div class="role">Consultant</div>
        <p>Business coach focused on practical results, helping teams lift productivity and communicate with confidence.</p>
      </div>
    </div>
  </div>
</section>

<section class="quick-links">
  <div class="wrap">
    <div class="quick-link"><svg width="60" height="48" viewBox="0 0 60 48" fill="#fff"><circle cx="20" cy="14" r="8"/><circle cx="40" cy="14" r="8"/><path d="M6 44c0-12 6-18 14-18s14 6 14 18z"/><path d="M28 44c0-12 4-18 12-18s14 6 14 18z"/></svg>Testimonials</div>
    <div class="quick-link"><svg width="60" height="48" viewBox="0 0 60 48" fill="none" stroke="#fff" stroke-width="3"><path d="M14 8h36v34H10a4 4 0 0 1-4-4V16h8"/><line x1="20" y1="18" x2="44" y2="18"/><line x1="20" y1="26" x2="44" y2="26"/><line x1="20" y1="34" x2="36" y2="34"/></svg>News</div>
    <div class="quick-link"><svg width="60" height="48" viewBox="0 0 60 48" fill="none" stroke="#fff" stroke-width="3"><path d="M8 8h44v24H26l-10 10v-10H8z"/></svg>Comments</div>
    <div class="quick-link"><svg width="60" height="48" viewBox="0 0 60 48" fill="none" stroke="#fff" stroke-width="3"><rect x="10" y="8" width="40" height="36" rx="2"/><line x1="10" y1="18" x2="50" y2="18"/><line x1="20" y1="3" x2="20" y2="12"/><line x1="40" y1="3" x2="40" y2="12"/></svg>Events</div>
  </div>
</section>

<section class="products">
  <div class="wrap">
    <h2 class="section-title">OUR PRODUCTS</h2>
    <p class="products-lead">Documents, Templates &amp; Business Systems. Here are just some of the documents, templates &amp; business systems that Marlowe Advisory has to offer. Please feel free to contact us directly should you be interested in purchasing any of our "ready to use" templates:</p>
    <div class="product-cols">
      <div class="product-col">
        <div class="product"><svg class="product-icon" viewBox="0 0 48 60" fill="#555"><circle cx="24" cy="10" r="8"/><path d="M12 22h24l-4 20h-4v16h-8V42h-4z"/></svg><div><h4>HR Documents</h4><ul><li>Position descriptions (generic)</li><li>Employee agreements (individualised to National Awards)</li><li>Conditions of employment</li><li>Inductions &amp; pro-forma</li></ul></div></div>
        <div class="product"><svg class="product-icon" viewBox="0 0 48 60" fill="#555"><circle cx="24" cy="10" r="8"/><path d="M12 22h24v20h-6v16H18V42h-6z"/></svg><div><h4>Operational</h4><ul><li>Position descriptions (generic)</li><li>Employee agreements (individualised to National Awards)</li><li>Conditions of employment</li><li>Inductions &amp; pro-forma</li></ul></div></div>
        <div class="product"><svg class="product-icon" viewBox="0 0 48 60" fill="#555"><rect x="6" y="8" width="36" height="46" rx="3"/><rect x="12" y="14" width="24" height="10" fill="#fff"/></svg><div><h4>Finance</h4><ul><li>Profit &amp; Loss Projections (forecasting)</li><li>New business start up costing</li><li>Budgets</li><li>Productivity reporting</li><li>Cash-flow Forecasting</li></ul></div></div>
      </div>
      <div class="product-col">
        <div class="product"><svg class="product-icon" viewBox="0 0 48 60" fill="#555"><circle cx="14" cy="10" r="7"/><circle cx="34" cy="10" r="7"/><path d="M4 22h20v36h-14zM24 22h20l-6 36H28z"/></svg><div><h4>Business Documents</h4><ul><li>Business plans</li><li>Strategic plans</li><li>Policies &amp; procedures (governance)</li><li>Functionality Charts</li><li>Letters and correspondence</li><li>Memos</li><li>Meeting Agendas</li><li>Induction Pro-forms</li><li>Tender submissions</li><li>Business proposals</li><li>Company Profiles</li><li>Advertising &amp; Marketing Plans</li></ul></div></div>
      </div>
    </div>
    <span class="products-next"></span>
  </div>
</section>

<section class="clients">
  <div class="wrap">
    <h2>CLIENTS</h2>
    <div class="client-row">
      <div class="client named">Brightline<br>Plumbing</div>
      <div class="client named">Northgate<br>Secure</div>
      <div class="client"></div>
      <div class="client"></div>
      <div class="client"></div>
    </div>
  </div>
</section>

<section class="contact">
  <div class="wrap">
    <h2 class="section-title">CONTACT US</h2>
    <div class="contact-body">
      <dl class="contact-details">
        <dt>Address</dt>
        <dd>PO Box 0000, Kelbridge, Victoria, Australia 3999</dd>
        <div class="row"><dt>Phone</dt><dd>03 5550 0199</dd></div>
        <div class="row"><dt>Email</dt><dd>admin@marloweadvisory-example.com.au</dd></div>
      </dl>
      <form class="contact-form">
        <div class="field">Email</div>
        <div class="field">Phone</div>
        <div class="field message">Message</div>
        <div class="submit"><svg width="12" height="12" viewBox="0 0 12 12"><circle cx="6" cy="6" r="6" fill="#1b9ad8"/></svg>Submit</div>
      </form>
    </div>
    <div class="contact-social"><span></span><span></span><span></span><span></span><span></span><span></span><span></span><span></span><span></span></div>
  </div>
</section>

<footer class="site-footer">
  <div class="brand"><span class="brand-dot"></span><span class="brand-name">MARLOWE ADVISORY</span></div>
  <div>COPYRIGHT © 2014 PRIVACY POLICY</div>
</footer>

</body>
</html>
```